Health Promotion Charity Info-graphic of 2013 Activities

We need an Info-graphic which will be printed on A4 for distribution to our members, government, key stakeholders and grant providers. It will also be uploaded to our website - www.brightsprout-youth.com.au

PROJECT BRIEF – Branding as per Brightsprout Youth Alliance
The aim of this infographic is to show the work that Brightsprout Youth Alliance did in 2013. It will be a pictorial annual report. It is to communicate to a wide audience the size and reach of Brightsprout Youth Alliance activities.
We are a health promotion charity that supports schools to deliver healthy food services and our aim is to improve food literacy so kids know what to eat, when.... Our aim is to reduce diet related disease - mainly those relating to overweight and obesity. The infographic should be in keeping with our brand - see www.brightsprout-youth.com.au

Using the following information
Our Members
In 2013 we had a total membership of 1,200
Our members are 1,137 Schools
20 Affiliates
24 Individuals
19 Leasees who operate 45 school canteens.
Our school members are
Public Sector Schools 846
Independent Schools 78
Catholic Schools 204
High schools 196
Primary 845
Central schools 30

There are 3082 schools in NSW – so we have 38% as members.

Our services
Supporting Schools
We answered 1078 enquiries through our telephone and email service.
We under took 20 menu assessments
22 school canteens had a business diagnostic
We flew to the regions and attended network meetings and school visits throughout New South Wales: South coast, Central Coast, north coast, illawarra, hunter new England and Dubbo

Publications
We produced the summer and winter editions of Brightsprout Tuckshop Digest magazine and
the Annual Brightsprout Tuckshop Supplier Directory.

Food Industry
We work with the food industry to change the nutritional value of food
There were 57 food companies that registered 823 food products suitable for school canteens. Of these products, 359 were Green products and 464 amber products.

Community Activities
We worked with Wendale and Corrigan councils delivering 8 school holiday cooking classes to 80 children and their parents.

WEBSITE STATS – www.brightsprout-youth.com.au
200,381 web visits
157,601 unique visitors
491.495 page views
2.45 pages per visitor

We worked with VORN to develop the Satchel Meals program which resulted in 79,289 Pocketa and Tabline Downloads and
10,629 subscribers to the weekly VORN email lunch box menu and shopping list.

Our funding
Total Income - $1,371,438
Government - $747,870 (54%)
Membership - $83,228 (6%)
Fee for Service – $42,946 (4%)
Other - $497,395(36%)
Total Equity $50,811

Colors
0555a3
9bcb3c
0593ce

```html
<!DOCTYPE html>
<html lang="en">
<head>
<meta charset="utf-8">
<title>Brightsprout Youth Alliance – 2013 in Review</title>
<link rel="stylesheet" href="https://fonts.googleapis.com/css2?family=Montserrat:wght@700;800&family=Noto+Serif:wght@400;700&family=Open+Sans:wght@300;400;700&display=swap">
<style>
  :root {
    --navy: #0555a3;
    --cyan: #0593ce;
    --lime: #9bcb3c;
    --ink: #0b3a78;
    --white: #ffffff;
    --head: "Montserrat", Arial, sans-serif;
    --serif: "Noto Serif", Georgia, serif;
    --sans: "Open Sans", Arial, sans-serif;
  }
  html, body { margin: 0; padding: 0; overflow: hidden; background: var(--white); }
  .sheet { position: relative; width: 849px; height: 1200px; overflow: hidden; background: var(--white); }
  .sheet > * { position: absolute; }
  .shapes { left: 0; top: 0; width: 849px; height: 1200px; }
  h2 { margin: 0; font-family: var(--head); font-weight: 800; text-transform: uppercase; letter-spacing: 0.3px; line-height: 1; }
  p { margin: 0; }
  b { font-weight: 700; }

  .members { left: 47px; top: 34px; width: 380px; color: var(--ink); }
  .members h2 { color: var(--navy); font-size: 29px; }
  .members p { font-family: var(--serif); font-size: 15px; line-height: 17px; }
  .members b { font-family: var(--head); font-weight: 800; color: var(--navy); }
  .members .gap { margin-top: 17px; }

  .brand { left: 47px; top: 410px; display: flex; align-items: center; gap: 10px;
    font-family: var(--head); font-weight: 800; font-size: 24px; color: var(--cyan); }
  .brand .dot { width: 36px; height: 36px; border-radius: 50%; background: var(--lime); }

  .panel { color: var(--white); }
  .panel h2 { font-size: 26px; color: var(--white); }
  .panel p { font-family: var(--sans); font-weight: 300; font-size: 15.5px; line-height: 17px; }
  .panel b { font-weight: 700; }

  .services { left: 537px; top: 37px; width: 285px; }
  .publications { left: 484px; top: 302px; width: 340px; }
  .industry { left: 484px; top: 466px; width: 340px; }

  .review { left: 45px; top: 566px; font-family: var(--head); font-weight: 800; font-size: 31px; color: var(--white); }

  .community { left: 242px; top: 691px; width: 560px; }
  .community p { font-weight: 400; font-size: 16px; line-height: 24px; margin-top: 8px; }

  .web { left: 450px; top: 848px; width: 380px; color: var(--white); }
  .web .url { font-family: var(--serif); font-size: 14px; margin-top: 3px; }
  .stats { display: grid; grid-template-columns: 162px 180px; row-gap: 6px; margin-top: 10px; }
  .stat { display: flex; align-items: center; gap: 8px; }
  .stat svg { flex: none; }
  .stat span { font-family: var(--serif); font-size: 15px; line-height: 16px; }
  .stat b { font-family: var(--head); font-weight: 800; display: block; }

  .satchel { left: 47px; top: 1017px; width: 245px; font-family: var(--sans); font-weight: 400;
    font-size: 15.5px; line-height: 22px; color: var(--white); }

  .funding-label { left: 344px; top: 1119px; width: 136px; text-align: center;
    font-family: var(--head); font-weight: 800; font-size: 22px; line-height: 28px; color: var(--white); }
  .funding { left: 561px; top: 1053px; font-family: var(--serif); font-size: 15.5px; line-height: 20.5px; color: var(--white); }
  .funding b { font-family: var(--head); font-weight: 800; font-size: 14.5px; }
</style>
</head>
<body>
<main class="sheet">

  <svg class="shapes" viewBox="0 0 849 1200" aria-hidden="true">
    <!-- services block -->
    <path d="M455 0 Q570 125 455 250 L849 250 L849 0 Z" fill="var(--navy)"/>
    <!-- publications -->
    <rect x="451" y="285" width="398" height="127" fill="var(--cyan)"/>
    <!-- food industry -->
    <rect x="451" y="449" width="398" height="181" fill="var(--lime)"/>
    <!-- review banner -->
    <path d="M0 540 L378 540 L395 585 L378 630 L0 630 Z" fill="var(--navy)"/>
    <path d="M0 550 L371 550 L385 585 L371 620 L0 620" fill="none" stroke="var(--white)" stroke-width="1.5" stroke-dasharray="5 4"/>
    <!-- community band -->
    <rect x="0" y="663" width="849" height="134" fill="var(--cyan)"/>
    <g fill="none" stroke="var(--white)" stroke-width="5">
      <polyline points="122,765 150,722 180,752 198,690"/>
      <circle cx="122" cy="765" r="10" fill="var(--cyan)"/>
      <circle cx="150" cy="722" r="10" fill="var(--cyan)"/>
      <circle cx="180" cy="752" r="10" fill="var(--cyan)"/>
      <circle cx="198" cy="690" r="10" fill="var(--cyan)"/>
    </g>
    <!-- website stats panel -->
    <path d="M400 832 L849 832 L849 985 L330 985 L305 950 L420 950 Z" fill="var(--lime)"/>
    <circle cx="365" cy="870" r="82" fill="var(--lime)"/>
    <circle cx="365" cy="870" r="66" fill="none" stroke="var(--white)" stroke-width="1.5" stroke-dasharray="4 4"/>
    <g fill="none" stroke="var(--white)" stroke-width="4">
      <circle cx="352" cy="872" r="30"/>
      <ellipse cx="352" cy="872" rx="13" ry="30"/>
      <line x1="322" y1="872" x2="382" y2="872"/>
      <line x1="327" y1="857" x2="377" y2="857"/>
      <line x1="327" y1="887" x2="377" y2="887"/>
    </g>
    <!-- satchel meals circle -->
    <circle cx="90" cy="1110" r="290" fill="var(--navy)"/>
    <g fill="var(--white)">
      <path d="M55 900 l18 -14 l14 14 l-6 6 l50 50 l-8 8 l-50 -50 l-6 6 Z"/>
      <path d="M120 895 a16 16 0 1 0 8 22 l-8 -2 l-4 -8 l4 -8 Z"/>
      <path d="M112 920 l-48 48 l8 8 l48 -48 Z"/>
    </g>
    <!-- funding panel -->
    <rect x="480" y="1030" width="369" height="170" fill="var(--cyan)"/>
    <circle cx="412" cy="1128" r="100" fill="var(--navy)" stroke="var(--white)" stroke-width="8"/>
    <text x="412" y="1095" text-anchor="middle" font-family="Montserrat, Arial, sans-serif" font-weight="700" font-size="64" fill="var(--white)">$</text>
  </svg>

  <section class="members">
    <h2>Our Members</h2>
    <p>In 2013 we had a total membership of 1,200</p>
    <p><b>1,137</b> Schools Members</p>
    <p><b>20</b> Affiliates</p>
    <p><b>24</b> Individuals</p>
    <p><b>19</b> Leasees who operate 45 school canteens.</p>
    <p class="gap">Our school members are</p>
    <p><b>846</b> Public Sector Schools</p>
    <p><b>78</b> Independent Schools</p>
    <p><b>204</b> Catholic Schools</p>
    <p><b>196</b> High schools</p>
    <p><b>845</b> Primary</p>
    <p><b>30</b> Central schools</p>
    <p class="gap">There are 3082 schools in NSW –<br>so we have 38% as members.</p>
  </section>

  <div class="brand"><span class="dot"></span>Brightsprout</div>

  <section class="panel services">
    <h2>Our Services</h2>
    <p>Supporting Schools<br>We answered <b>1078</b> enquiries through our telephone and email service. We under took <b>20</b> menu assessments <b>22</b> school canteens had a business diagnostic. We flew to the regions and attended network meetings and school visits throughout New South Wales</p>
  </section>

  <section class="panel publications">
    <h2>Publications</h2>
    <p>We produced the summer and winter editions of Brightsprout Tuckshop Digest magazine and the Annual Brightsprout Tuckshop Supplier Directory.</p>
  </section>

  <section class="panel industry">
    <h2>Food Industry</h2>
    <p>We work with the food industry to change the nutritional value of food<br>There were <b>57</b> food companies that registered <b>823</b> food products suitable for school canteens. Of these products, <b>359</b> were Green products and <b>464</b> amber products.</p>
  </section>

  <div class="review">2013 IN REVIEW</div>

  <section class="panel community">
    <h2>Community Activities</h2>
    <p>We worked with Wendale and Corrigan councils delivering<br><b>8</b> school holiday cooking classes to <b>80</b> children and their parents.</p>
  </section>

  <section class="web">
    <h2>Website Stats</h2>
    <p class="url">www.brightsprout-youth.com.au</p>
    <div class="stats">
      <div class="stat">
        <svg width="22" height="22" viewBox="0 0 22 22" aria-hidden="true"><circle cx="11" cy="11" r="11" fill="var(--white)"/><circle cx="11" cy="11" r="6" fill="none" stroke="var(--lime)" stroke-width="2"/></svg>
        <span><b>200,381</b>web visits</span>
      </div>
      <div class="stat">
        <svg width="24" height="24" viewBox="0 0 24 24" aria-hidden="true"><circle cx="12" cy="12" r="10.5" fill="none" stroke="var(--white)" stroke-width="2"/><polyline points="7,12 11,16 17,8" fill="none" stroke="var(--white)" stroke-width="2"/></svg>
        <span><b>491.495</b>page views</span>
      </div>
      <div class="stat">
        <svg width="22" height="22" viewBox="0 0 22 22" aria-hidden="true"><circle cx="11" cy="11" r="11" fill="var(--white)"/><circle cx="11" cy="8" r="3" fill="var(--lime)"/><rect x="6.5" y="12" width="9" height="5" rx="2" fill="var(--lime)"/></svg>
        <span><b>157,601</b>unique visitors</span>
      </div>
      <div class="stat">
        <svg width="24" height="24" viewBox="0 0 24 24" aria-hidden="true"><circle cx="12" cy="12" r="10.5" fill="none" stroke="var(--white)" stroke-width="2"/><circle cx="11" cy="11" r="4" fill="none" stroke="var(--white)" stroke-width="2"/><line x1="14" y1="14" x2="17.5" y2="17.5" stroke="var(--white)" stroke-width="2"/></svg>
        <span><b>2.45</b>pages per visitor</span>
      </div>
    </div>
  </section>

  <p class="satchel">We worked with VORN to develop the Satchel Meals program which resulted in <b>79,289</b> Pocketa and Tabline Downloads and <b>10,629</b> subscribers to the weekly VORN email lunch box menu and shopping list.</p>

  <div class="funding-label">OUR<br>FUNDING</div>

  <section class="funding">
    <p><b>$1,371,438</b> Total Income</p>
    <p><b>$747,870 (54%)</b> Government</p>
    <p><b>$83,228 (6%)</b> Membership</p>
    <p><b>$42,946 (4%)</b> Fee for Service</p>
    <p><b>$497,395(36%)</b> Other</p>
    <p><b>$50,811</b> Total Equity</p>
  </section>

</main>
</body>
</html>
```